Layout the contents of the Home page of a web-site using a defined template

ParvenFILE is software for managing electronic documents.
In technical terms it is defined as a document management system.

```html
<!DOCTYPE html>
<html lang="en">
<head>
<meta charset="utf-8">
<title>ParvenFILE – Document Management System</title>
<link href="https://fonts.googleapis.com/css2?family=Arimo:wght@400;700&display=swap" rel="stylesheet">
<style>
:root{
  --orange:#f7931e;
  --orange-dark:#e2781a;
  --ink:#333;
  --text:#555;
  --muted:#777;
  --line:#ddd;
  --bar:#3a3a3a;
  --page:#f4f5f7;
  --white:#fff;
  --navy:#2b4a6f;
  --blue-head:#1c5fb8;
}
*{box-sizing:border-box;margin:0;padding:0}
html,body{width:755px;height:1200px;overflow:hidden}
body{position:relative;background:var(--white);font-family:'Arimo',Arial,sans-serif;color:var(--text);font-size:8.5px;line-height:1.6}
.abs{position:absolute}
.page-top{left:0;top:0;width:755px;height:416px;background:var(--page)}
.topline{left:0;top:0;width:755px;height:3px;background:#444}
.util{left:412px;top:5px;width:306px;height:17px;background:var(--white);display:flex;align-items:center;gap:9px;padding-left:44px;font-size:7px;color:#444}
.share{border:1px solid #ccc;border-radius:2px;padding:0 4px;font-size:7px;line-height:11px;background:#f7f7f7}
.share b{color:#c33}
.share.post b{color:#2a7fc1}
.logo{left:34px;top:25px;width:228px;height:44px;background:var(--white);display:flex;align-items:center;gap:6px;padding-left:2px}
.logo-mark{width:26px;height:26px;background:var(--orange)}
.logo-name{font-weight:700;font-size:22px;color:#444;letter-spacing:.5px;line-height:1}
.logo-sub{font-size:9px;color:#666;margin-top:3px}
.live{left:550px;top:71px;font-size:9px;font-weight:700;color:#444;display:flex;align-items:center;gap:4px}
.live i{display:block;width:11px;height:8px;background:var(--orange);border-radius:1px}
.flags{left:667px;top:75px;display:flex;gap:5px}
.flags span{width:12px;height:8px;display:block}
.nav{left:35px;top:88px;width:684px;height:40px;background:var(--white);border-bottom:4px solid var(--bar);display:flex;align-items:center}
.nav-item{font-size:12.5px;color:#444;padding:0 10px;height:36px;display:flex;align-items:center;gap:4px;text-transform:uppercase}
.nav-item i{display:inline-block;width:8px;height:8px;background:#444;position:relative}
.nav-item.active{background:var(--orange);color:var(--white);padding:0 11px}
.nav-item.active i{background:var(--white)}
.search{margin-left:auto;margin-right:12px;width:112px;height:21px;border:1px solid #eee;font-size:9px;color:#888;display:flex;align-items:center;gap:6px;padding-left:5px}
.dropdown{z-index:10;left:35px;top:131px;width:179px;height:80px;background:var(--white);box-shadow:0 2px 5px rgba(0,0,0,.15);display:grid;grid-template-columns:1fr 1fr;grid-auto-rows:18px;padding:8px 0 0 17px;font-size:8px;color:#555;line-height:18px}
.slider{left:44px;top:153px;width:663px;height:219px;background:linear-gradient(90deg,#8c8f96,#c9c3b5 40%,#e4dfd3 70%,#cfc9bb)}
.slide-head{left:430px;top:192px;font-size:17px;font-weight:700;color:var(--blue-head);letter-spacing:-.2px}
.slide-text{left:432px;top:217px;width:270px;font-size:10.5px;color:#111;line-height:1.3}
.arrow{width:24px;height:24px;border-radius:50%;background:#eee;border:2px solid #999;display:flex;align-items:center;justify-content:center}
.dots{left:346px;top:384px;display:flex;gap:2px}
.dots span{width:8px;height:8px;border-radius:50%;background:#999}
.dots span.on{background:#555}
.hatch{height:4px;background:repeating-linear-gradient(90deg,#bbb 0 2px,transparent 2px 4px)}
.card{background:var(--white);border:1px solid #e3e3e3}
.tabs{left:42px;top:443px;display:flex;gap:2px}
.tab{width:104px;height:34px;font-size:9.5px;font-weight:700;text-transform:uppercase;line-height:1.3;padding:6px 0 0 12px;background:#c8c8c8;color:#8a8a8a}
.tab.on{background:var(--white);color:#333;border:1px solid #ddd;border-bottom:0}
h2.sub{font-size:10px;font-weight:400;color:#333}
p{font-size:8px;color:#666;line-height:14.3px}
a.hl{color:var(--orange);text-decoration:none}
.h-big{font-size:14px;font-weight:700;color:#444;text-transform:uppercase;line-height:1.2;letter-spacing:.2px}
.photo{display:block}
.btn-orange{background:var(--orange);color:var(--white);font-size:8px;border-radius:4px;padding:2px 6px;display:inline-block}
.btn-dark{background:var(--navy);color:var(--white);font-size:8px;border-radius:5px;padding:2px 7px;display:inline-block}
.tryit{left:570px;top:477px;width:83px;height:26px;background:var(--orange);border:2px solid #f2c36e;color:#b64b00;font-size:12.5px;font-weight:700;text-align:center;line-height:22px}
.drive{left:566px;width:141px;border-bottom:1px solid #eee;font-size:8.5px;line-height:1.3;color:#444}
.drive b{font-weight:700;font-size:9px;text-transform:uppercase;color:#333}
.news-head{left:553px;top:642px;width:163px;height:27px;background:var(--orange);color:var(--white);font-size:15px;font-weight:700;text-align:center;line-height:27px;text-transform:uppercase}
.news{left:561px;width:150px;font-size:8px;color:#444;line-height:13.5px}
.news .t{color:var(--orange);font-size:9px}
.partners{left:37px;top:870px;width:681px;height:60px;background:var(--white);display:flex;align-items:center;justify-content:space-around;padding:0 10px}
.partners span{display:block;height:30px;background:#d8d8d8;border-radius:3px}
.pnav{top:890px;width:24px;height:20px;background:#222;display:flex;align-items:center;justify-content:center}
.foot{top:956px;width:210px}
.foot h3{font-size:12.5px;font-weight:700;color:#333;border-bottom:3px solid #bbb;padding-bottom:2px;margin-bottom:6px}
.foot li{list-style:none;font-size:8px;color:#555;height:28.5px;line-height:26px;border-bottom:1px dashed #ddd;display:flex;align-items:center;gap:4px}
.foot li:last-child{border-bottom:0}
.foot li i{display:block;width:7px;height:7px;border-radius:50%;background:var(--orange)}
.about{font-size:8px;line-height:14.3px;color:#555;text-align:justify}
.bottom-rule{left:35px;top:1146px;width:684px;height:3px;background:var(--orange)}
.legal{left:230px;top:1161px;width:300px;text-align:center;font-size:7px;color:#666;line-height:14px}
.online{left:567px;top:1166px;width:152px;height:34px;background:linear-gradient(#f9a54a,var(--orange-dark));border-radius:6px 6px 0 0;color:var(--white);font-size:9.5px;display:flex;align-items:center;padding-left:17px;gap:4px}
.online i{display:block;width:8px;height:8px;border-radius:50%;background:#5bd35b}
</style>
</head>
<body>
<div class="abs page-top"></div>
<div class="abs topline"></div>

<header>
  <div class="abs util">
    <span>Buy</span><span>Free Trial</span><span>Blog</span><span>Contact</span>
    <span class="share"><b>Share</b> 956</span>
    <span class="share post"><b>Post</b> 12K</span>
  </div>
  <div class="abs logo">
    <span class="logo-mark"></span>
    <div><div class="logo-name">ParvenFILE</div><div class="logo-sub">Document Management System</div></div>
  </div>
  <div class="abs live"><i></i>Live Support</div>
  <div class="abs flags">
    <span style="background:#1f3c88"></span>
    <span style="background:linear-gradient(90deg,#2a9b3a 33%,#fff 33% 66%,#d22 66%)"></span>
    <span style="background:linear-gradient(#c11 25%,#f5c400 25% 75%,#c11 75%)"></span>
  </div>
  <nav class="abs nav">
    <div class="nav-item active">Product<i></i></div>
    <div class="nav-item">Features<i></i></div>
    <div class="nav-item">Solutions<i></i></div>
    <div class="nav-item">Resources<i></i></div>
    <div class="nav-item">Partners<i></i></div>
    <div class="search">
      <svg width="10" height="10" viewBox="0 0 10 10"><circle cx="6" cy="4" r="3" fill="none" stroke="#333" stroke-width="1.4"/><line x1="4" y1="6" x2="1" y2="9" stroke="#333" stroke-width="1.6"/></svg>search...
    </div>
  </nav>
</header>

<section>
  <div class="abs slider" role="img" aria-label="Office worker buried between tall stacks of paper files"></div>
  <div class="abs slide-head">SPEED UP YOUR BUSINESS....</div>
  <div class="abs slide-text">Take advantage of document managment to cut the information retrieval time from hours to seconds</div>
  <div class="abs arrow" style="left:48px;top:249px"><svg width="8" height="10"><path d="M6 1 2 5 6 9" fill="none" stroke="#222" stroke-width="2"/></svg></div>
  <div class="abs arrow" style="left:677px;top:249px"><svg width="8" height="10"><path d="M2 1 6 5 2 9" fill="none" stroke="#222" stroke-width="2"/></svg></div>
  <div class="abs dots"><span></span><span></span><span></span><span class="on"></span><span></span></div>
</section>

<div class="abs dropdown">
  <span>Overview</span><span>Features</span>
  <span>Cloud and SaaS</span><span>Free Trial</span>
  <span>Buy</span><span>Latest Release</span>
</div>

<div class="abs hatch" style="left:35px;top:430px;width:684px"></div>

<main>
  <div class="abs card" style="left:35px;top:476px;width:328px;height:193px"></div>
  <div class="abs tabs">
    <div class="tab on">Document<br>Management</div>
    <div class="tab">Knowledge<br>Management</div>
    <div class="tab">New in<br>Version 6.4</div>
  </div>
  <div class="abs" style="left:49px;top:484px;width:298px">
    <h2 class="sub">Document Management Software &amp; Online</h2>
    <p style="margin-top:4px">ParvenFILE is an intuitive and highly performant <a class="hl">document management system</a> that offers the power of enterprise document management to mid-size companies and large organizations. ParvenFILE helps any kind of organizations all around the world to gain control over their documents, with particular focus on fast content retrieval and business process automation.</p>
    <p style="margin-top:10px">Our solution enables your team to create, co-author, and coordinate any amount of documents. With ParvenFILE you will increase collaboration and productivity via next-generation web interface, integration into Macrowrite® Office and Mailroom, and automatic import from your shared folders.</p>
  </div>

  <div class="abs card" style="left:35px;top:684px;width:328px;height:155px"></div>
  <div class="abs h-big" style="left:49px;top:691px;width:298px;border-bottom:1px solid #ddd;padding-bottom:4px">Easy Document Management</div>
  <div class="abs photo" style="left:52px;top:729px;width:199px;height:77px;background:linear-gradient(90deg,#6f6a66,#b9aba0 50%,#8c8a8a)" role="img" aria-label="Team of colleagues joining hands in a high five"></div>
  <p class="abs" style="left:256px;top:728px;width:97px;text-align:justify;line-height:13.5px">ParvenFILE is a document management system targeted to business users. The solution is designed to be very user friendly.</p>
  <span class="abs btn-orange" style="left:52px;top:813px">Read more</span>

  <div class="abs" style="left:377px;top:443px;width:1px;height:396px;background:#e6e6e6"></div>
  <div class="abs h-big" style="left:389px;top:444px;width:150px">ParvenFILE for<br>Mobile</div>
  <div class="abs" style="left:389px;top:494px;width:56px;height:56px;background:var(--navy)" role="img" aria-label="Mobile platform badge"></div>
  <p class="abs" style="left:448px;top:491px;width:92px">This software provides an user friendly web interface, which ensures high adoption by users and return on</p>
  <p class="abs" style="left:389px;top:575px;width:148px">The broad set of standardized and unique functions makes ParvenFILE suitable in any document manage-</p>
  <div class="abs" style="left:389px;top:657px;width:50px;height:50px;background:linear-gradient(#dcdcdc,#8a8a8a)" role="img" aria-label="Business woman using a smartphone"></div>
  <p class="abs" style="left:448px;top:655px;width:92px">Search and see docu-ments directly on your Droidix phone, read and share your com-pany's documents in a</p>
  <p class="abs" style="left:389px;top:735px;width:150px">All this from the ParvenFILE easy and lightweight Gleam Droidix App.</p>
  <span class="abs btn-dark" style="left:387px;top:769px">Read more</span>

  <div class="abs" style="left:551px;top:443px;width:1px;height:396px;background:#e6e6e6"></div>
  <div class="abs" style="left:717px;top:443px;width:1px;height:396px;background:#e6e6e6"></div>
  <div class="abs h-big" style="left:561px;top:446px;font-size:15px">Test Drive</div>
  <div class="abs tryit">Try Now</div>
  <div class="abs drive" style="top:517px;height:27px"><b>Download</b><br>A feature-rich Enterprise Edition</div>
  <div class="abs drive" style="top:547px;height:27px"><b>Get</b><br>The open source</div>
  <div class="abs drive" style="top:577px;height:27px"><b>Access</b><br>The demo online</div>
  <div class="abs drive" style="top:607px;height:27px;border:0"><b>Comute</b><br>The Savings</div>
  <div class="abs news-head">Product News</div>
  <div class="abs news" style="top:674px"><div class="t">New release 6.4</div>The new release of the product is made available for download, multi workspaces and retention policies are just some of the new features.</div>
  <div class="abs news" style="top:747px"><div class="t">Welcome to Australia</div>New strategic agreement for the marketing and commercial operations in Australia and Oceania region.</div>
  <span class="abs btn-orange" style="left:560px;top:818px">More news</span>
</main>

<div class="abs hatch" style="left:35px;top:866px;width:684px"></div>
<div class="abs partners">
  <span style="width:58px;border-radius:15px"></span>
  <span style="width:104px"></span>
  <span style="width:75px"></span>
  <span style="width:70px"></span>
  <span style="width:66px"></span>
  <span style="width:95px"></span>
  <span style="width:82px"></span>
</div>
<div class="abs pnav" style="left:14px;border-radius:10px 0 0 10px"><svg width="6" height="8"><path d="M5 0 1 4 5 8" fill="none" stroke="#fff" stroke-width="1.8"/></svg></div>
<div class="abs pnav" style="left:717px;border-radius:0 10px 10px 0"><svg width="6" height="8"><path d="M1 0 5 4 1 8" fill="none" stroke="#fff" stroke-width="1.8"/></svg></div>
<div class="abs hatch" style="left:35px;top:932px;width:684px"></div>

<footer>
  <div class="abs foot" style="left:44px">
    <h3>ParvenFILE</h3>
    <ul>
      <li><i></i>Document Management System Features</li>
      <li><i></i>Commercial Editions</li>
      <li><i></i>Open Source Document Management</li>
      <li><i></i>Hosted Document Management System</li>
      <li><i></i>Online Demo</li>
    </ul>
  </div>
  <div class="abs foot" style="left:274px">
    <h3>Document Management Solutions</h3>
    <ul>
      <li><i></i>Paperless Office</li>
      <li><i></i>Legal Document Management Software</li>
      <li><i></i>Knowledge Management System</li>
      <li><i></i>Version Control System</li>
      <li><i></i>Health Care</li>
    </ul>
  </div>
  <div class="abs foot" style="left:512px;width:201px">
    <h3>About Us</h3>
    <p class="about">ParvenFILE is a document management software easy-to-use, reliable and affordable, which can improve the efficiency of your company to help you find, manage and share documents. The software is available in over 10 languages and lets you quickly access the information contained in the documents of your organization. Records management, workflow, version control, and auditing are some of the features of the software.</p>
  </div>

  <div class="abs bottom-rule"></div>
  <div class="abs" style="left:703px;top:1149px;width:16px;height:9px;background:var(--orange)"></div>
  <div class="abs" style="left:35px;top:1164px;width:10px;height:10px;background:var(--orange);border-radius:2px"></div>
  <div class="abs" style="left:52px;top:1164px;width:58px;height:11px;background:#777"></div>
  <div class="abs" style="left:115px;top:1164px;width:59px;height:11px;background:#eee;border:1px solid #ccc;border-radius:2px"></div>
  <div class="abs legal">Contact Us &nbsp;|&nbsp; Privacy Policy &nbsp;|&nbsp; Support &nbsp;|&nbsp; Resources<br>Copyright © 2011 Parven Labs Srl - p.iva 04127730588. All Rights Reserved.</div>
  <div class="abs online"><i></i><b>Online</b>&nbsp; Live support</div>
</footer>
</body>
</html>
```